Vorin Co Premium Matcha brand Label

This is a label design project for a luxury tea brand. Feel free to be creative within the guidelines.
Attached to this project is a document called “Private Label Design Requirements” with the design guidelines and template. There is another document called "Vorin Co Packaging Instructions" this has more details necessary to stick to the guidelines in the first document.

I have also attached the certifications to be included as well as different variations of the logo for you to use.

If you have any questions, I am here.

Need extra days to review

Young, active, fun, enjoy the finer things

```html
<!DOCTYPE html>
<html lang="en">
<head>
<meta charset="utf-8">
<title>Vorin Co Premium Matcha Label</title>
<link rel="stylesheet" href="https://fonts.googleapis.com/css2?family=Cinzel:wght@400&family=Marcellus&family=Open+Sans:wght@400;600&display=swap">
<style>
  :root {
    --backdrop: #9aa3a1;
    --green-light: #86c44a;
    --green-deep: #5a9f2c;
    --cream: #eef1e0;
    --cream-shade: #dfe6c8;
    --matcha: #5e9e2a;
    --ink: #2f3a26;
    --white: #ffffff;
    --logo-dark: #1b1b1b;
  }
  * { box-sizing: border-box; margin: 0; padding: 0; }
  html, body { width: 1088px; height: 1200px; overflow: hidden; }
  body {
    background: var(--backdrop);
    font-family: "Open Sans", sans-serif;
    position: relative;
  }
  .label {
    position: absolute;
    left: 32px; top: 490px;
    width: 1024px; height: 220px;
    display: flex;
    box-shadow: 0 6px 18px rgba(0,0,0,.18);
  }
  .panel { position: relative; height: 100%; }
  .panel--side {
    width: 340px;
    background: linear-gradient(180deg, var(--green-light), var(--green-deep));
    color: var(--white);
  }
  .panel--front {
    width: 344px;
    background: radial-gradient(ellipse at center, var(--cream) 55%, var(--cream-shade));
    color: var(--matcha);
    text-align: center;
  }
  .botanical {
    position: absolute;
    border-radius: 40%;
    background: radial-gradient(circle at 45% 40%, rgba(255,255,255,.85), rgba(255,255,255,.35) 45%, rgba(70,150,40,.55) 75%, transparent 80%);
  }
  .botanical--left { left: 8px; top: 30px; width: 130px; height: 160px; }
  .botanical--right { right: 10px; top: 30px; width: 130px; height: 160px; }
  .leaf-edge {
    position: absolute; top: 20px; width: 42px; height: 180px;
    background: linear-gradient(90deg, rgba(90,160,45,.75), rgba(90,160,45,.15));
    border-radius: 50%;
  }
  .leaf-edge--left { left: 0; }
  .leaf-edge--right { right: 0; transform: scaleX(-1); }

  .ingredients { position: absolute; left: 150px; top: 34px; width: 180px; }
  .ingredients__title { font-size: 14px; font-weight: 600; margin-bottom: 6px; }
  .ingredients__text { font-size: 13px; line-height: 1.25; }
  .rule { width: 60px; height: 1px; background: var(--white); margin: 14px 0 12px; }
  .directions { list-style: none; font-size: 11.5px; line-height: 1.5; }
  .directions li::before { content: "• "; }

  .brand { margin-top: 28px; display: inline-flex; align-items: center; gap: 7px; }
  .brand__mark { width: 14px; height: 14px; background: var(--logo-dark); }
  .brand__name { font-family: "Open Sans", sans-serif; font-weight: 600; font-size: 15px; color: var(--logo-dark); }
  .grade {
    margin-top: 14px;
    font-family: "Marcellus", serif; font-size: 16px; color: var(--ink);
    display: flex; align-items: center; justify-content: center; gap: 8px;
  }
  .grade::before, .grade::after { content: ""; width: 22px; height: 1px; background: var(--ink); }
  .product-name {
    font-family: "Cinzel", serif; font-size: 62px; line-height: 1; letter-spacing: 2px;
    margin-top: 2px; color: var(--matcha);
  }
  .net-weight { font-size: 12px; font-weight: 600; color: var(--ink); margin-top: 8px; }

  .distributor { position: absolute; left: 22px; top: 70px; font-size: 9.5px; line-height: 1.6; }
  .certs { position: absolute; left: 22px; top: 128px; display: flex; align-items: center; gap: 6px; }
  .cert--square { width: 26px; height: 26px; background: var(--white); border-radius: 3px; }
  .cert--round { width: 26px; height: 26px; background: var(--white); border-radius: 50%; }
  .storage { font-size: 10.5px; font-weight: 600; line-height: 1.25; margin-left: 6px; text-transform: uppercase; }
</style>
</head>
<body>
  <main class="label">
    <section class="panel panel--side panel--ingredients">
      <div class="botanical botanical--left" role="img" aria-label="White flower and green leaf illustration"></div>
      <div class="ingredients">
        <h2 class="ingredients__title">Ingredients</h2>
        <p class="ingredients__text">Premium Organic Japanese Matcha Green Tea</p>
        <div class="rule"></div>
        <ul class="directions">
          <li>2 tsp of Matcha</li>
          <li>2oz of Water (170-180 degree F)</li>
          <li>Whisk in a W formation until frothy</li>
          <li>Sweeten to taste</li>
        </ul>
      </div>
    </section>

    <section class="panel panel--front">
      <div class="leaf-edge leaf-edge--left" role="img" aria-label="Green leaf illustration"></div>
      <div class="leaf-edge leaf-edge--right" role="img" aria-label="Green leaf illustration"></div>
      <div class="brand">
        <span class="brand__mark"></span>
        <span class="brand__name">Vorin Co</span>
      </div>
      <p class="grade">Premium Organic Ceremonial</p>
      <h1 class="product-name">MATCHA</h1>
      <p class="net-weight">Net Wt: 30g (1.06oz)</p>
    </section>

    <section class="panel panel--side panel--info">
      <p class="distributor">
        Distributed by Vorin Co | Larkfield, Ga<br>
        Certified Organic by Fenwell<br>
        PRODUCT OF JAPAN
      </p>
      <div class="certs">
        <span class="cert--square"></span>
        <span class="cert--round"></span>
        <p class="storage">Keep refrigerated<br>for quality</p>
      </div>
      <div class="botanical botanical--right" role="img" aria-label="White flower and green leaf illustration"></div>
    </section>
  </main>
</body>
</html>
```